Modern Business Card for Lanternfield 2018

Our company assumes the best about people. We are creating an online community of entrepreneurs and business leaders who struggle with marketing their business online.

This business card should POP! We recently got a new logo and are launching a new website next month, so our business cards should make a statement that feels:
-Fresh
-Smart
-Trustworthy
-Fun

Target Market(s)

small business owners, entrepreneurs

Industry/Entity Type

Digital Marketing

Contact Information for Business Card

Dimensions: 3.5" x 2"

Font styles to use
Sans Serif

Colors
f37122
ffffff

Requirements
Must have
• We need a business card with a modern, bold design. We will use one side of the card as a lead-generation offer, so text on one side will need to fit up to 140 characters. The business card should stick to our core colors (orange, black, and white).
Nice to have
• We think a vertical "portrait" design could be interesting.
Should not have
• Should not look like a traditional business card. The round icon should stand out from a distance.

```html
<!DOCTYPE html>
<html lang="en">
<head>
<meta charset="utf-8">
<title>Lanternfield Business Card</title>
<link rel="stylesheet" href="https://fonts.googleapis.com/css2?family=Montserrat:wght@400;600;700;800;900&display=swap">
<style>
  :root {
    --orange: #f37122;
    --white: #ffffff;
    --black: #1f1f1f;
    --ink: #222222;
    --backdrop: #2b2d30;
  }
  * { box-sizing: border-box; margin: 0; padding: 0; }
  html, body { width: 1200px; height: 900px; overflow: hidden; }
  body {
    background: var(--backdrop);
    font-family: "Montserrat", sans-serif;
    display: flex;
    flex-direction: column;
    align-items: center;
    justify-content: center;
    gap: 40px;
  }
  .card {
    position: relative;
    width: 700px;
    height: 400px;
    border-radius: 26px;
    overflow: hidden;
    background: var(--white);
  }

  /* Offer side */
  .offer-band {
    position: absolute; left: 0; top: 0; width: 100%; height: 132px;
    background: var(--orange);
    display: flex; justify-content: space-between; align-items: flex-start;
    padding: 16px 38px 0;
    color: var(--white);
  }
  .benefit { line-height: 1; }
  .benefit--center { text-align: center; margin-top: 20px; }
  .benefit--right { text-align: right; margin-top: 40px; }
  .benefit__verb { font-weight: 800; font-size: 30px; letter-spacing: 0.5px; }
  .benefit__gain { font-weight: 400; font-size: 19px; margin-top: 3px; }
  .pointer {
    position: absolute; left: 50%; width: 30px; height: 16px; transform: translateX(-50%);
  }
  .pointer--down { top: 132px; background: var(--orange); clip-path: polygon(0 0, 100% 0, 50% 100%); }
  .pointer--up { top: 226px; background: var(--black); clip-path: polygon(50% 0, 100% 100%, 0 100%); }
  .brand {
    position: absolute; left: 0; top: 140px; width: 100%; height: 96px;
    display: flex; flex-direction: column; align-items: center; justify-content: center;
  }
  .brand__lockup { display: flex; align-items: center; gap: 14px; }
  .brand__dot { width: 46px; height: 46px; border-radius: 50%; background: var(--orange); }
  .brand__name { font-weight: 800; font-size: 38px; color: var(--ink); letter-spacing: 0.5px; line-height: 1; }
  .brand__tagline {
    font-family: "Montserrat", sans-serif; font-weight: 700; font-size: 14px; color: var(--ink);
    margin-top: 6px; margin-left: 60px; letter-spacing: 1px;
  }
  .offer {
    position: absolute; left: 0; top: 242px; width: 100%; height: 158px;
    background: var(--black); color: var(--white);
    display: flex; flex-direction: column; align-items: center; justify-content: center;
    font-weight: 400; font-size: 19px; line-height: 1.5; letter-spacing: 1px; text-align: center;
  }
  .offer__link { color: var(--orange); font-weight: 800; }
  .offer__link span { color: var(--white); }

  /* Contact side */
  .edge { position: absolute; top: 0; height: 100%; }
  .edge--left { left: 0; width: 20px; background: var(--orange); }
  .edge--right { right: 0; width: 20px; background: var(--black); }
  .notch { position: absolute; width: 16px; height: 30px; }
  .notch--left { left: 20px; top: 44px; background: var(--orange); clip-path: polygon(0 0, 100% 50%, 0 100%); }
  .notch--right { right: 20px; bottom: 44px; background: var(--black); clip-path: polygon(100% 0, 100% 100%, 0 50%); }
  .contact {
    position: absolute; inset: 0;
    display: flex; flex-direction: column; align-items: center; justify-content: center;
  }
  .contact__name {
    font-family: "Montserrat", sans-serif; font-weight: 900; font-size: 52px; color: var(--ink);
    letter-spacing: 1px; line-height: 1;
  }
  .divider { display: flex; align-items: center; gap: 14px; margin: 24px 0 20px; }
  .divider__line { width: 150px; height: 3px; background: var(--orange); }
  .divider__dot { width: 38px; height: 38px; border-radius: 50%; background: var(--orange); }
  .contact__role { font-weight: 800; font-size: 22px; color: var(--ink); letter-spacing: 1px; }
  .contact__email { font-weight: 400; font-size: 20px; color: var(--ink); letter-spacing: 1px; margin-top: 4px; }
</style>
</head>
<body>
  <section class="card card--offer">
    <div class="offer-band">
      <div class="benefit"><div class="benefit__verb">REACH</div><div class="benefit__gain">more people</div></div>
      <div class="benefit benefit--center"><div class="benefit__verb">MAKE</div><div class="benefit__gain">more money</div></div>
      <div class="benefit benefit--right"><div class="benefit__verb">CREATE</div><div class="benefit__gain">more impact</div></div>
    </div>
    <div class="pointer pointer--down"></div>
    <div class="brand">
      <div class="brand__lockup">
        <div class="brand__dot"></div>
        <div class="brand__name">LANTERNFIELDNOW</div>
      </div>
      <div class="brand__tagline">TELL STORIES THAT INSPIRE ACTION</div>
    </div>
    <div class="pointer pointer--up"></div>
    <div class="offer">
      <p>GET YOUR FREE LANTERNFIELD STARTER PACKAGE AND OUR</p>
      <p>MARKETING GUIDE TODAY AT <span class="offer__link">LANTERNFIELD<span>NOW</span>.COM/START</span></p>
    </div>
  </section>

  <section class="card card--contact">
    <div class="edge edge--left"></div>
    <div class="notch notch--left"></div>
    <div class="edge edge--right"></div>
    <div class="notch notch--right"></div>
    <div class="contact">
      <h1 class="contact__name">OWEN MARLOW</h1>
      <div class="divider">
        <div class="divider__line"></div>
        <div class="divider__dot"></div>
        <div class="divider__line"></div>
      </div>
      <p class="contact__role">STORY MARKETING COACH</p>
      <p class="contact__email">OWEN@LANTERNFIELDNOW.COM</p>
    </div>
  </section>
</body>
</html>
```